Logo for Internal Medicine practice

I want a logo for my Internal Medicine practice, I would like it to be with my name on it which is Lorena Benítez Prado.

I would like the business card to say the following (it is in Spanish since my practice is in Spanish):

Lorena Benítez Prado
Medicina Interna
Cel. 5587316420
lorenabenitezprado@correovela.com

Logo Text

Lorena Benítez

```html
<!DOCTYPE html>
<html lang="es">
<head>
<meta charset="utf-8">
<title>Lorena Benítez — Tarjeta de presentación</title>
<link rel="stylesheet" href="https://fonts.googleapis.com/css2?family=Poppins:wght@400;500;800&display=swap">
<style>
  :root {
    --stage: #2b2b2b;
    --ink: #0b0b0b;
    --paper: #ffffff;
    --brand-red: #e31e24;
    --faint: #ececec;
    --muted: #9a9a9a;
  }
  * { box-sizing: border-box; margin: 0; padding: 0; }
  html, body {
    width: 1200px; height: 900px; overflow: hidden;
    background: var(--stage);
    font-family: "Poppins", sans-serif;
  }
  .canvas { position: relative; width: 1200px; height: 900px; }
  .card {
    position: absolute; left: 250px;
    width: 700px; height: 400px;
    border-radius: 28px; overflow: hidden;
  }
  .card--back { top: 35px; background: var(--ink); }
  .card--front { top: 465px; background: var(--paper); }

  /* brand lockup */
  .lockup { position: absolute; display: flex; flex-direction: column; align-items: flex-end; }
  .lockup__mark {
    width: 110px; height: 110px;
    background: var(--brand-red);
    border: 6px solid var(--paper);
    outline: 2px solid var(--ink);
    align-self: center;
    margin-bottom: 14px;
  }
  .card--back .lockup__mark { outline-color: var(--paper); border-color: var(--ink); }
  .lockup__name {
    font-weight: 800; font-size: 34px; line-height: 1;
    color: var(--brand-red); text-transform: uppercase; letter-spacing: 1px;
  }
  .lockup__tagline {
    margin-top: 6px; font-size: 11px; font-weight: 400;
    letter-spacing: 4.6px; text-transform: uppercase; color: var(--muted);
  }
  .card--back .lockup { left: 50%; top: 82px; transform: translateX(-50%); }
  .card--back .lockup__tagline { color: #d0d0d0; }
  .card--front .lockup { right: 44px; top: 26px; }
  .card--front .lockup__mark { margin-right: 30px; }

  .faint-block { position: absolute; left: 40px; top: 40px; width: 180px; height: 180px; background: var(--faint); }

  .decor { position: absolute; left: 0; top: 0; width: 700px; height: 400px; }

  .holder { position: absolute; left: 40px; top: 226px; }
  .holder__name { font-weight: 800; font-size: 25px; color: var(--ink); text-transform: uppercase; letter-spacing: .5px; line-height: 1.1; }
  .holder__role { font-weight: 500; font-size: 20px; color: var(--brand-red); margin-top: 2px; }
  .contact { list-style: none; margin-top: 10px; }
  .contact__item { display: flex; align-items: center; gap: 12px; font-size: 17px; color: var(--ink); line-height: 1.7; }
  .contact__icon { width: 22px; height: 22px; flex: none; }
</style>
</head>
<body>
<main class="canvas">

  <section class="card card--back" aria-label="Reverso de la tarjeta">
    <div class="lockup">
      <div class="lockup__mark"></div>
      <div class="lockup__name">Lorena Benítez</div>
      <div class="lockup__tagline">Internal Medicine Practice</div>
    </div>
  </section>

  <section class="card card--front" aria-label="Frente de la tarjeta">
    <div class="faint-block"></div>

    <svg class="decor" viewBox="0 0 700 400" aria-hidden="true">
      <line x1="350" y1="262" x2="560" y2="220" stroke="var(--ink)" stroke-width="3"/>
      <polyline points="566,220 598,214 606,200 612,230 618,208 624,212 680,202"
                fill="none" stroke="var(--brand-red)" stroke-width="3" stroke-linejoin="round"/>
      <polygon points="0,378 430,378 452,400 0,400" fill="var(--brand-red)"/>
      <polygon points="430,366 700,366 700,400 460,400" fill="var(--ink)"/>
      <polygon points="430,366 442,366 464,400 452,400" fill="var(--paper)"/>
    </svg>

    <div class="lockup">
      <div class="lockup__mark"></div>
      <div class="lockup__name">Lorena Benítez</div>
      <div class="lockup__tagline">Internal Medicine Practice</div>
    </div>

    <div class="holder">
      <h1 class="holder__name">Lorena Benítez Prado</h1>
      <p class="holder__role">Medicina Interna</p>
      <ul class="contact">
        <li class="contact__item">
          <svg class="contact__icon" viewBox="0 0 22 22" aria-hidden="true">
            <rect width="22" height="22" fill="var(--brand-red)"/>
            <rect x="7" y="4" width="8" height="14" rx="1.5" fill="none" stroke="#fff" stroke-width="1.6"/>
            <circle cx="11" cy="15.5" r="0.9" fill="#fff"/>
          </svg>
          <span>5587316420</span>
        </li>
        <li class="contact__item">
          <svg class="contact__icon" viewBox="0 0 22 22" aria-hidden="true">
            <rect width="22" height="22" fill="var(--brand-red)"/>
            <rect x="4" y="6" width="14" height="10" fill="none" stroke="#fff" stroke-width="1.6"/>
            <polyline points="4,6 11,12 18,6" fill="none" stroke="#fff" stroke-width="1.6"/>
          </svg>
          <span>lorenabenitezprado@correovela.com</span>
        </li>
      </ul>
    </div>
  </section>

</main>
</body>
</html>
```